Wordpress Website for Kestrel Path Youth Support Initiative

We are looking for a wordpress website that is clean, crisp and bold for our Kestrel Path Youth Support Initiative.

We are a Canadian hospital in Winnipeg, MB which sees many youth injured by violence. We are starting up an Kestrel Path Youth Support Initiative for youth injured by violence. The youth who we will serve will be between the age of 14 - 24 and many will be gang-involved.

However, it is important to note that this website isn't for the youth themselves as much as it is for professionals and community interested in learning about our program. As such, it is should be friendly but professional. I am interested in a bold, crisp look.

I have attached our logo file for your use.
Updates

I forgot to mention that there should be a section along the bottom to include logos of funders and partners.

Also would be nice to include a spot for viewers to automatically subscribe to our newsletter by putting their email in.

I have added in a file of text that I will use - but want to easily be able to change and update (and post links etc). 

Target Market(s)

This will target a professional and community audience. We would like a crisp, bold, professional presence

Industry/Entity Type

Hospital

Requirements
Must have
• I would like a navigation bar that includes the following:

About KP-YSI (Background and Research sections)
People
Latest News
Job Opportunities
Research Opportunities
Publications & Reports
Contact KP-YSI ( a form)

I would also like a search form and a link to plimzo.

While I am comfortable with Wordpress - I am not an expert. I want this to be as simple as possible for me to update.
Nice to have
• We have a great logo and only a few photos which I will upload in the next day.

We could also use stock photos for now but overtime switch these with photos of our own hospital emergency department and team. Additionally, we would like some stock photos of youth - a diverse mix but to include Aboriginal/First Nations, immigrant and caucasian youth
Should not have
• This design should not have guns, knifes, alcohol or blood/gore in there (I've learned to state this after using pixel harbor for the logo! )

```html
<!DOCTYPE html>
<html lang="en">
<head>
<meta charset="utf-8">
<title>Kestrel Path Youth Support Initiative</title>
<link href="https://fonts.googleapis.com/css2?family=Arimo:ital,wght@0,400;0,700;1,400;1,700&family=Arvo:wght@700&family=Open+Sans:wght@400;600&display=swap" rel="stylesheet">
<style>
:root{
  --red:#8c1b24;
  --red-dark:#7a141c;
  --text:#555;
  --heading:#444;
  --line:#dcdcdc;
  --band:#efefef;
}
*{box-sizing:border-box;margin:0;padding:0}
html,body{width:1019px;height:1200px;overflow:hidden}
body{position:relative;background:linear-gradient(180deg,#fafafa 0,#f3f3f3 60%,#fff 100%);font-family:"Arimo",Arial,sans-serif;color:var(--text)}
.top-rule{position:absolute;top:0;left:0;width:100%;height:3px;background:#bdbdbd}
.brand{position:absolute;left:110px;top:18px;display:flex;align-items:center;gap:14px}
.brand-square{width:58px;height:58px;background:var(--red)}
.brand-name{font-family:"Open Sans",sans-serif;font-weight:400;font-size:13.5px;line-height:16px;color:#666}
.util-links{position:absolute;right:111px;top:13px;font-family:"Open Sans",sans-serif;font-size:9.5px;color:#444}
.util-links span{margin:0 4px;color:#999}
.phone{position:absolute;right:111px;top:50px;display:flex;align-items:center;gap:12px;font-weight:700;font-size:17px;color:var(--red)}
.nav{position:absolute;left:110px;top:98px;width:798px;height:39px;background:linear-gradient(180deg,#9b2029,var(--red-dark));border-radius:2px;display:flex;align-items:center;justify-content:space-between;padding:0 18px 0 12px}
.nav a{font-family:"Open Sans",sans-serif;font-size:12px;color:#fff;text-decoration:none}
.hero{position:absolute;left:110px;top:144px;width:798px;height:312px;border:1px solid #ddd;background:linear-gradient(90deg,#f2f2f2 0,#e8e8e8 40%,#b08b7a 55%,#7e4b4f 75%,#6d7e4e 100%);overflow:hidden}
.hero-photo{position:absolute;right:0;top:0;width:430px;height:100%;background:linear-gradient(100deg,rgba(240,240,240,0) 0,#a97f70 25%,#7b3642 55%,#557041 100%)}
.hero h1{position:absolute;left:28px;top:100px;font-family:"Arvo",serif;font-weight:700;font-size:28px;line-height:36px;color:#4a4a4a;letter-spacing:.4px}
.hero-arrows{position:absolute;left:28px;top:282px;display:flex;gap:8px}
.card{position:absolute;top:478px;width:255px;height:236px;background:#fff;border:1px solid var(--line);border-radius:2px;padding:9px 10px}
.card h2{font-family:"Open Sans",sans-serif;font-weight:400;font-size:15.5px;color:var(--red);margin-bottom:7px}
.card .thumb{width:233px;height:85px;border:1px solid #ccc;margin-bottom:12px}
.card p{font-size:10.5px;line-height:15.3px;color:var(--text)}
.card p em{color:var(--red)}
.card h3{font-style:italic;font-weight:700;font-size:12px;color:#333;margin-bottom:2px}
.more{display:block;text-align:right;font-size:9.8px;font-weight:700;color:var(--red);text-decoration:none;margin-top:5px}
.section-rule{position:absolute;left:110px;top:736px;width:798px;height:3px;background:var(--red-dark)}
.col{position:absolute;top:766px}
.col h2{font-family:"Open Sans",sans-serif;font-weight:400;font-size:17px;color:var(--heading);margin-bottom:8px}
.col h2 span{color:var(--red)}
.col p{font-size:10.6px;line-height:19.5px;color:var(--text)}
.col .more{text-align:left;margin-top:10px}
.pub-thumb{float:left;width:83px;height:66px;margin:0 12px 4px 0;border:1px solid #ccc;background:linear-gradient(135deg,#eee,#a9a9a9 50%,#d8d8d8)}
.news-date{font-weight:700;font-size:11px;color:var(--red);margin-bottom:7px;letter-spacing:.3px}
.news-title{font-style:italic;font-size:12px;line-height:15px;color:#333;margin-bottom:4px}
.col .news-body{line-height:17px}
.partners{position:absolute;left:0;top:995px;width:100%;height:112px;background:var(--band);border-top:1px solid #ddd;border-bottom:1px solid #ddd}
.partners h2{position:absolute;left:128px;top:30px;width:84px;text-align:center;font-family:"Open Sans",sans-serif;font-weight:400;font-size:17px;line-height:20px;color:var(--red)}
.partner{position:absolute;top:31px;width:125px;height:60px;background:#fff;border:1px solid #ccc;display:flex;align-items:center;justify-content:center}
.partner i{display:block;width:80px;height:26px;background:#d9d9d9;border-radius:3px}
.footer-copy{position:absolute;left:110px;top:1128px;font-size:10.2px;line-height:20px;color:#666}
.footer-copy b{color:var(--red)}
.footer-copy span{margin:0 5px}
.signup{position:absolute;left:522px;top:1127px}
.signup h3,.connect h3{font-size:11px;font-weight:700;color:var(--red);margin-bottom:8px}
.signup-row{display:flex;gap:7px}
.signup-input{width:160px;height:25px;border:1px solid #ccc;background:#eee;border-radius:2px;font-style:italic;font-size:10px;color:#999;padding:6px 11px}
.signup-btn{width:60px;height:25px;background:var(--red);color:#fff;font-size:10.5px;font-weight:700;border-radius:2px;display:flex;align-items:center;justify-content:center;letter-spacing:.4px}
.connect{position:absolute;left:813px;top:1127px}
.social{display:flex;gap:9px}
.social i{display:block;width:26px;height:26px;border-radius:3px}
</style>
</head>
<body>
<div class="top-rule"></div>

<header>
  <div class="brand">
    <div class="brand-square"></div>
    <div class="brand-name">Kestrel Path<br>Youth Support<br>Initiative</div>
  </div>
  <div class="util-links">Home<span>|</span>Contact Us<span>|</span>FAQ<span>|</span>Site Map</div>
  <div class="phone">
    <svg width="23" height="23" viewBox="0 0 23 23"><circle cx="11.5" cy="11.5" r="11.5" fill="#d9453c"/><path d="M8 6.5c.6-.4 1.2-.3 1.5.2l1 1.8c.3.5.2 1-.3 1.3l-.7.5c.5 1.3 1.4 2.3 2.6 3l.6-.6c.4-.4 1-.4 1.4-.1l1.7 1.1c.5.3.6.9.2 1.4l-.8 1c-.5.6-1.4.7-2.3.3-2.8-1.3-4.8-3.5-5.7-6.4-.3-.9 0-1.8.8-2.5z" fill="#fff"/></svg>
    204 555 0148
  </div>
  <nav class="nav">
    <a>Home</a><a>About Us</a><a>People</a><a>Latest News</a><a>Job Opportunities</a><a>Research Opportunities</a><a>Publications &amp; Reports</a>
  </nav>
</header>

<section class="hero">
  <div class="hero-photo" role="img" aria-label="Photo of a smiling father carrying his son on his back outdoors"></div>
  <h1>WrapAround Care for<br>Youth Injured by<br>Violence..</h1>
  <div class="hero-arrows">
    <svg width="18" height="18" viewBox="0 0 18 18"><circle cx="9" cy="9" r="9" fill="#8a8a8a"/><path d="M10.5 5.5 7 9l3.5 3.5" stroke="#fff" stroke-width="1.6" fill="none"/></svg>
    <svg width="18" height="18" viewBox="0 0 18 18"><circle cx="9" cy="9" r="9" fill="#111"/><path d="M7.5 5.5 11 9l-3.5 3.5" stroke="#fff" stroke-width="1.6" fill="none"/></svg>
  </div>
</section>

<article class="card" style="left:110px">
  <h2>KP YSI Research</h2>
  <div class="thumb" role="img" aria-label="Photo of a man comforting a child beside a flag" style="background:linear-gradient(90deg,#3d4e8a 0,#c9333d 25%,#8a6a5e 55%,#b52a2e 100%)"></div>
  <p>The <em>“WrapAround Care for Youth Injured by Violence”</em> Study is a pilot randomized control trial designed to examining recruitment, feasibility and program safety prior to launching a larger effectiveness trial.</p>
  <a class="more">LEARN MORE &gt;&gt;</a>
</article>

<article class="card" style="left:382px">
  <h2>People</h2>
  <div class="thumb" role="img" aria-label="Portrait photo of a smiling physician" style="background:linear-gradient(90deg,#8c8c8c 0,#bdbdbd 40%,#d8b48a 65%,#e9e4dc 100%)"></div>
  <h3>Maren Tollefsen</h3>
  <p>Dr. Maren Tollefsen, is an emergency physician and researcher in youth violence in Winnipeg, Manitoba. Dr. Tollefsen graduated from Northfield Medical School in 2003..</p>
  <a class="more">LEARN MORE &gt;&gt;</a>
</article>

<article class="card" style="left:654px">
  <h2>Research Opportunities</h2>
  <div class="thumb" role="img" aria-label="Photo of a doctor with a stethoscope examining a patient" style="background:linear-gradient(90deg,#b9b0a8 0,#eef3f6 30%,#7fc3de 55%,#e8e8e8 80%,#5a3a30 100%)"></div>
  <p>Please contact Dr. Tollefsen at <em>mtollefsen@kpysi.ca</em> if you are interested in research with the KP-YSI. Dr. Tollefsen is currently accepting students inter-ested in Graduate, BSc Med and undergraduate summer student positions.</p>
  <a class="more">LEARN MORE &gt;&gt;</a>
</article>

<div class="section-rule"></div>

<section class="col" style="left:112px;width:240px">
  <h2>Welcome to <span>KP-YSI</span></h2>
  <p>Youth injured by violence is a concerning issue in Canada. Youth homicide is the fourth most common reason of death among youth in Canada and in some provinces, the most common reason for visiting an emergency department. Even more concerning is that there is a high repeat rate of visits to emergency departments for subsequent injuries caused by violence.</p>
  <a class="more">LEARN MORE &gt;&gt;</a>
</section>

<section class="col" style="left:382px;width:255px">
  <h2>Publication &amp; Reports</h2>
  <p><span class="pub-thumb" role="img" aria-label="Photo of a stack of newspapers"></span>Aliquam molestie, mi et imperdiet euismod, dui purus auctor tellus, et interdum lacus lectus et ante. Sed accumsan sollicitudin sapien, sit amet adipiscing turpis gravida ac. Vestibu-lum ante ipsum primis in faucibus orci luctus et ultrices posuere cubilia...</p>
  <a class="more" style="margin-top:6px">LEARN MORE &gt;&gt;</a>
</section>

<section class="col" style="left:664px;width:248px">
  <h2>Latest News</h2>
  <div class="news-date">JUINE20, 2013</div>
  <div class="news-title">Youth Violence Research Program &nbsp;at Prairie Institute...</div>
  <p class="news-body">“WrapAround Care for Youth Injured by Violence: A Pilot Randomized Control Trial”..These operating grants were received from the Canadian Council for Health Inquiry and Prairie Institute of Child Health.</p>
  <a class="more">LEARN MORE &gt;&gt;</a>
</section>

<section class="partners">
  <h2>Funders<br>&amp;<br>Partners</h2>
  <div class="partner" style="left:229px"><i></i></div>
  <div class="partner" style="left:367px"><i></i></div>
  <div class="partner" style="left:505px"><i></i></div>
  <div class="partner" style="left:643px"><i></i></div>
  <div class="partner" style="left:781px"><i></i></div>
</section>

<footer>
  <div class="footer-copy">Copyright © 2013. <b>KP YSI</b><br>All Right Reserved. Terms<span>|</span>Privacy<span>|</span>Sitemap</div>
  <div class="signup">
    <h3>Newsletter SignUp</h3>
    <div class="signup-row"><div class="signup-input">Enter Email</div><div class="signup-btn">SIGN UP</div></div>
  </div>
  <div class="connect">
    <h3>Connect Us</h3>
    <div class="social">
      <i style="background:#3b5b98" role="img" aria-label="Folio"></i>
      <i style="background:#3fb0d8" role="img" aria-label="plimzo"></i>
      <i style="background:#2a7bb3" role="img" aria-label="Linkro"></i>
    </div>
  </div>
</footer>
</body>
</html>
```